Brookvale Animal Clinic Relocation Business Card

We are relocating our business from a shopping center location to a brand-new facility about 2 miles down the road directly on the main square of A small town that is a suburb of Charlotte North Carolina. I would like for the cards to indicate that we plan to be moving in September 2014. I would like to have a sort of map that shows people the easiest way to get there from two separate directions. I would also like to have our logo and maybe an image of the new building in the background on the back of the card. I just want to get the word out what we are doing and let people know how easy it is to get there. I uploaded elevations from the architect of the new building and would like to use the one on the bottom sort of in the background on the back of the card if possible, or the front. I have also attached some sketches of the best direction to get there. The purple lines would show the recommended route. The one labeled 1 would come from one direction and the one labeled 2 comes from the current location. I don't know if we should do totally separate cards with the back having the map show from each different direction or if we should somehow have both maps on the same card. On the front I would like to have our logo and the new address as well as our phone number. New Address: 482 East Corwin Street, larkdale NC 28417. Phone (same) 704.316.5928 I would also like to have our website on there. Brookvaleac.com as far as route number two it is important to show people that they can take this small road called Main Street (for some reason) and bypass the majority of the traffic, especially that occurs at the elementary school. This is through a small neighborhood but is certainly used by people cutting through. The Gulvix station is pretty familiar to most folks as well and obviously the fact that that is the main intersection in downtown Matthews. Monroe Road and Highway 51 is a very large intersection that people are familiar with. Maybe both sides could basically be identical of the card just with the different directions on each side? Thank you!

```html
<!DOCTYPE html>
<html lang="en">
<head>
<meta charset="utf-8">
<title>Brookvale Animal Clinic – Business Cards</title>
<link href="https://fonts.googleapis.com/css2?family=Exo+2:ital,wght@0,400;0,500;0,600;1,500&display=swap" rel="stylesheet">
<style>
  :root {
    --backdrop: #8e8f91;
    --card: #f3f4f5;
    --card-edge: #e4e5e7;
    --brand-blue: #0b74c1;
    --route: #7a4fb0;
    --map-bg: #e6ebf0;
    --ink: #2a2c30;
    --muted: #55585d;
  }
  * { box-sizing: border-box; margin: 0; padding: 0; }
  html, body { width: 1200px; height: 894px; overflow: hidden; }
  body {
    background: var(--backdrop);
    font-family: "Exo 2", "Segoe UI", sans-serif;
    position: relative;
  }
  .card {
    position: absolute;
    width: 560px;
    height: 320px;
    background: linear-gradient(135deg, #ffffff 0%, var(--card) 60%, var(--card-edge) 100%);
    overflow: hidden;
  }
  .card--front { left: 60px; top: 470px; }
  .card--back { left: 580px; top: 110px; }

  .band {
    position: absolute;
    right: 0;
    background: var(--brand-blue);
    border-radius: 999px 0 0 999px;
  }
  .card--front .band { left: 410px; top: 140px; height: 72px; }
  .card--back .band { left: 360px; top: 160px; height: 88px; }

  /* Front */
  .person__name {
    position: absolute; left: 40px; top: 30px;
    color: var(--brand-blue); font-size: 25px; font-weight: 500; font-style: italic; line-height: 30px;
  }
  .person__role {
    position: absolute; left: 40px; top: 62px;
    color: var(--muted); font-size: 10px; letter-spacing: 0.08em; text-transform: uppercase;
  }
  .rule { position: absolute; height: 2px; background: var(--brand-blue); }
  .rule--name { left: 36px; top: 80px; width: 300px; }
  .rule--address { left: 36px; top: 216px; width: 524px; height: 1.5px; }
  .rule--foot-a { left: 36px; top: 264px; width: 524px; }
  .rule--foot-b { left: 36px; top: 280px; width: 524px; height: 1px; }

  .contact {
    position: absolute; left: 40px; top: 92px;
    display: grid; grid-template-columns: 80px auto; row-gap: 2px;
    font-size: 16px; line-height: 20px;
  }
  .contact dt { color: var(--brand-blue); }
  .contact dd { color: var(--ink); letter-spacing: 0.04em; }

  .pin { position: absolute; left: 38px; top: 192px; width: 14px; height: 20px; }
  .address {
    position: absolute; left: 40px; top: 228px;
    color: var(--ink); font-size: 16px; letter-spacing: 0.06em;
  }

  /* Back */
  .building {
    position: absolute; left: 0; right: 0; bottom: 0; height: 70px;
    background: linear-gradient(180deg, rgba(11,116,193,0) 0%, rgba(11,116,193,0.12) 100%);
  }
  .brand {
    position: absolute; left: 40px; top: 28px;
    display: flex; align-items: center; gap: 10px;
  }
  .brand__dot { width: 22px; height: 22px; border-radius: 50%; background: var(--brand-blue); }
  .brand__name { color: var(--brand-blue); font-size: 19px; font-weight: 500; }

  .notice {
    position: absolute; left: 40px; top: 64px;
    color: var(--ink); font-size: 13px; line-height: 18px; letter-spacing: 0.03em;
  }
  .notice__lead { color: var(--brand-blue); font-weight: 600; font-size: 15px; }

  .routes {
    position: absolute; left: 40px; top: 132px;
    display: flex; gap: 14px;
  }
  .route { width: 140px; }
  .route__map {
    width: 140px; height: 96px; border: 1px solid var(--brand-blue);
    background: var(--map-bg);
  }
  .route__label {
    margin-top: 4px; color: var(--route); font-size: 12px; font-weight: 500;
  }
  .card--back .contact-line {
    position: absolute; right: 24px; top: 268px;
    color: var(--ink); font-size: 13px; letter-spacing: 0.04em;
  }
</style>
</head>
<body>
  <section class="card card--back" aria-label="Card back">
    <div class="building" role="img" aria-label="Faint elevation of the new clinic building"></div>
    <div class="brand">
      <span class="brand__dot"></span>
      <span class="brand__name">Brookvale Animal Clinic</span>
    </div>
    <p class="notice">
      <span class="notice__lead">We're moving — September 2014</span><br>
      482 East Corwin Street, larkdale NC 28417
    </p>
    <div class="routes">
      <figure class="route">
        <div class="route__map" role="img" aria-label="Route map 1 to the new clinic"></div>
        <figcaption class="route__label">Route 1</figcaption>
      </figure>
      <figure class="route">
        <div class="route__map" role="img" aria-label="Route map 2 from the current location via Main Street"></div>
        <figcaption class="route__label">Route 2 · from current site</figcaption>
      </figure>
    </div>
    <div class="band"></div>
    <p class="contact-line">704.316.5928 · Brookvaleac.com</p>
  </section>

  <section class="card card--front" aria-label="Card front">
    <h1 class="person__name">Daniel Hartley</h1>
    <p class="person__role">General Manager</p>
    <div class="rule rule--name"></div>
    <dl class="contact">
      <dt>Phone:</dt><dd>704 316 5928</dd>
      <dt>Fax:</dt><dd>704 316 5928</dd>
      <dt>Email:</dt><dd>info@brookvaleac.com</dd>
      <dt>website:</dt><dd>www.brookvaleac.com</dd>
    </dl>
    <svg class="pin" viewBox="0 0 16 22" aria-hidden="true">
      <path d="M8 0C3.6 0 0 3.5 0 7.8 0 13.5 8 22 8 22s8-8.5 8-14.2C16 3.5 12.4 0 8 0z" fill="var(--brand-blue)"/>
      <circle cx="8" cy="7.8" r="3" fill="#fff"/>
    </svg>
    <div class="rule rule--address"></div>
    <p class="address">482 East Corwin Street, larkdale NC</p>
    <div class="rule rule--foot-a"></div>
    <div class="rule rule--foot-b"></div>
    <div class="band"></div>
  </section>
</body>
</html>
```